Flyer Required for Economics Tuition business in Singapore

Require a 4-page, A4 bi-fold full colour flyer. To use attractive & vibrant colours. Can make use of colour schemes and design layouts from upcoming website revamp: http://lessonmaple.com/Website/
Target audience for the flyer will be 17 - 18 years old A Level students in Singapore studying in Junior Colleges.
I have attached the detailed design brief with the content required for the flyer as a file titled "Design Brief.docx" & also the logo for our business to be used in the flyer & optional photos that can be used in the flyer

```html
<!DOCTYPE html>
<html lang="en">
<head>
<meta charset="utf-8">
<title>Economics At LessonMaple – Flyer Spread</title>
<link href="https://fonts.googleapis.com/css2?family=Archivo+Black&family=Arimo:ital,wght@0,400;0,700;1,700&family=Encode+Sans+Condensed:wght@400;700&display=swap" rel="stylesheet">
<style>
  :root{
    --orange:#f7941d;
    --ink:#1a1a1a;
    --body:#2b2b2b;
    --red:#d4141c;
    --page-left:#e4e6ef;
    --page-right:#f2f3f8;
    --stage:#d9d9dc;
    --white:#ffffff;
  }
  *{box-sizing:border-box;margin:0;padding:0}
  html,body{width:1200px;height:994px;overflow:hidden;background:var(--stage)}
  .spread{position:absolute;left:0;top:72px;width:1200px;height:849px;overflow:hidden;font-family:"Arimo",Arial,sans-serif;color:var(--body)}
  .page{position:absolute;top:0;width:600px;height:849px;overflow:hidden}
  .page--left{left:0;background:linear-gradient(180deg,#eef0f6 0%,var(--page-left) 60%,#d9dce7 100%)}
  .page--right{left:600px;background:linear-gradient(90deg,#ffffff 0%,var(--page-right) 100%)}
  .photo{position:absolute}
  .photo--group-top{left:0;top:0;width:600px;height:183px;background:linear-gradient(180deg,#c9ccd4 0%,#8a8f9e 55%,#3f4a63 100%)}
  .frame{position:absolute;border:4px solid var(--white);box-shadow:0 2px 6px rgba(0,0,0,.35)}
  .frame--one{left:-12px;top:192px;width:268px;height:180px;transform:rotate(-4deg);background:linear-gradient(180deg,#e9eaee 0%,#b7bac6 60%,#6b6f80 100%)}
  .frame--two{left:-8px;top:380px;width:276px;height:175px;transform:rotate(3deg);background:linear-gradient(180deg,#cfd2dc 0%,#7d7682 55%,#3d3a48 100%)}
  .frame--three{left:-8px;top:558px;width:276px;height:180px;transform:rotate(-3deg);background:linear-gradient(180deg,#f0f0f2 0%,#c5c4c8 55%,#404048 100%)}
  .founder{position:absolute;left:292px;top:200px;width:286px;height:550px}
  .founder h1{font-family:"Archivo Black",Arial,sans-serif;font-weight:400;font-size:23px;line-height:27px;color:var(--ink);padding-bottom:8px;border-bottom:1px solid #333;width:283px;white-space:nowrap}
  .founder section{position:absolute;left:0;width:275px}
  .founder h2{font-size:13px;font-weight:700;color:var(--ink);margin-bottom:6px}
  .founder p{font-size:8.3px;line-height:12px}
  .founder__background{top:80px}
  .founder__academic{top:152px}
  .founder__teaching{top:263px}
  .founder__style{top:386px}
  .footer{position:absolute;left:0;top:753px;width:1200px;height:84px;background:var(--orange)}
  .footer::after{content:"";position:absolute;left:0;top:84px;width:1200px;height:12px;background:#c9cbd6}
  .url{position:absolute;top:32px;font-size:16.5px;letter-spacing:1.8px;color:var(--white)}
  .brand{position:absolute;top:32px;color:var(--white);font-weight:700;font-size:16.5px;line-height:20px;white-space:nowrap}
  .quote-box{position:absolute;left:19px;top:0;width:279px;height:238px;background:var(--orange)}
  .quote-box::after{content:"";position:absolute;left:24px;top:238px;border-left:20px solid transparent;border-top:18px solid var(--orange)}
  .quote-mark{position:absolute;font-family:"Arimo",Arial,sans-serif;font-weight:700;font-size:170px;line-height:1;color:var(--white)}
  .quote-mark--open{left:12px;top:-28px}
  .quote-mark--close{left:200px;top:158px}
  .quote-box h1{position:absolute;left:18px;top:88px;font-family:"Encode Sans Condensed","Arial Narrow",sans-serif;font-weight:700;font-size:52px;line-height:52px;color:var(--ink);letter-spacing:-.5px;white-space:nowrap}
  .quote-box h1 span{display:block;font-weight:400;font-size:39px;line-height:40px;letter-spacing:.3px;margin-left:4px}
  .testimonials{position:absolute;width:250px}
  .testimonials--left{left:35px;top:282px}
  .testimonials--right{left:317px;top:103px}
  .testimonial{margin-bottom:11px}
  .testimonial p{font-size:7.5px;line-height:10px}
  .testimonial cite{display:block;margin-left:109px;font-style:italic;font-weight:700;font-size:7.5px;line-height:10px;color:var(--red)}
  .testimonials--right .testimonial{margin-bottom:12px}
  .photo--lecture{left:0;top:539px;width:600px;height:206px;background:linear-gradient(90deg,#e38a3a 0%,#9a5f3c 40%,#6b5a58 70%,#d9d6d8 100%)}
</style>
</head>
<body>
<main class="spread">
  <section class="page page--left">
    <div class="photo photo--group-top" role="img" aria-label="Group photo of smiling students pointing towards the camera"></div>
    <div class="frame frame--one" role="img" aria-label="Photo of a class of students seated in rows"></div>
    <div class="frame frame--two" role="img" aria-label="Photo of students posing in front of the learning centre sign"></div>
    <div class="frame frame--three" role="img" aria-label="Photo of students sitting on a sofa"></div>

    <article class="founder">
      <h1>About our<br>Programme Founder</h1>
      <section class="founder__background">
        <h2>Background</h2>
        <p>Mr Adrian Lim is the Programme Founder &amp; Managing Director for Economics At LessonMaple Pte Ltd. He also owns and manages Bright Path Education Centre &amp; Idea Lab Learning Centre.</p>
      </section>
      <section class="founder__academic">
        <h2>Academic Qualifications</h2>
        <p>Mr Lim loves and specialises in Economics and he obtained his Bachelor of Arts in Economics from the Northbay University (NBU). He is also currently doing his Masters in Applied. Economics at the Harbourview Management University (HMU) and he intends to pursue further studies in Economics after his Masters..</p>
      </section>
      <section class="founder__teaching">
        <h2>Teaching Experience</h2>
        <p>Mr Lim has established a unique tuition programme under the name of Economics at LessonMaple since 2007. Each year he tutors about 150-200 on average and many of his students were top students in their classes and level for Economics. (read the testimonials!) That means more than a thousand students have gone through Mr Lim's intensive Economics tuition programme!</p>
      </section>
      <section class="founder__style">
        <h2>Style of Teaching</h2>
        <p>Mr Lim is different from other tutors because he employs a mixture of strategies to help the student excel. He thinks that for a student to excel in a subject, he must first be interested in the subject, and that's why Mr Lim tries to make his lessons interesting and relatable to the student. He also looks at the syllabus holistically and reverse engineers the methods to do well for the examination by ensuring that the appropriate right amount of content is covered without compromising on the quality of the learning. Through weekly discussions and looking at real-world problems, Mr Lim also helps his students discover the essential application skills that are required to score that Distinction in the A Levels.</p>
      </section>
    </article>
  </section>

  <section class="page page--right">
    <div class="quote-box">
      <span class="quote-mark quote-mark--open">&ldquo;</span>
      <span class="quote-mark quote-mark--close">&rdquo;</span>
      <h1>Testimonials<span>From Students</span></h1>
    </div>

    <div class="testimonials testimonials--left">
      <blockquote class="testimonial"><p>Mr Lim really has all his students' interests at heart. He buys dinner for us, provide us with mini snckbars, incentivise us with great rewards; there was also once where he bought me some flu medicine because I was suffering from a bad cold thank you Mr Lim!</p><cite>Tan Mei Ling<br>Eastbridge Junior College</cite></blockquote>
      <blockquote class="testimonial"><p>Mr Lim is a very friendly teacher who ensures that his students receive the best. He spends a lot of effort in preparing for lessons such as finding articles that are relevant to the subject and coming up with different ways to help us learn better.</p><cite>Goh Wei Jie<br>Riverside Junior College</cite></blockquote>
      <blockquote class="testimonial"><p>Mr Lim's lessons are very engaging and fun. It's a very different and beneficial tuition style that will definitely benefit students. Content was covered very effectively and thoroughly for each lesson and made easy to understand by Mr Lim's effective teaching methods and anecdotal examples. There is a very comfortable environment here ad especially so since there are free refreshments. It has been very enjoyable being in this tuition and Mr Lim is a wonderful tutor.</p><cite>Lee Hui Min Clara<br>Hillcrest High School</cite></blockquote>
    </div>

    <div class="testimonials testimonials--right">
      <blockquote class="testimonial"><p>Even though I have only been working with Mr Lim for a few months, I have learnt many different skills and specific Singaporean examples that are essential for a good economic grade, but not covered in school classes. Mr Lim also has amazing stories to tell, and I personally am inspired by his 'pilot' story.</p><cite>Ryan Chua<br>Westfield Institution</cite></blockquote>
      <blockquote class="testimonial"><p>Mr Lim and the tuition centre has greatly improves my quality of work in economics and his knowledge and insights provided during lessons were very valuable to me as an econs student I was able to perform well in almost all my examinations after attending lessons and this gave me confidence closing in onto A levels. I would recommend this tuition centre to those in need of help in econs. You can acquire relevant skills in essays and CSQ which I believe will help me pull thru A levels with ease.</p><cite>Jonas Teo<br>Northgate Junior College</cite></blockquote>
      <blockquote class="testimonial"><p>Mr Lim is a very friendly and approachable tutor who makes economic concepts much easier to understand. His lessons are very well paced and effective and it has helped me increased my school test grades by 3 grades. tuition@ lessonmaple has been fun and very helpful.</p><cite>Koh Jun Hao<br>Westfield Institution</cite></blockquote>
      <blockquote class="testimonial"><p>Mr Lim is a very engaging tutor who never fail to pique our interest and curiosity over the economics concepts and the current economy situation. He makes an effort to make interesting analogies to ensure that his students understand certain concepts thoroughly. Kudos!</p><cite>Sarah Wong Li Ting<br>Westfield Institution</cite></blockquote>
      <blockquote class="testimonial"><p>I find Mr Lim a committed tutor who does research to provide us with many economics articles and practices for the class. I get much more fruitful practices on essays and case studies during lessons from the group discussions and timed practices that allow me to gauge my understanding knowledge of the topic. Thanks Mr Lim for providing such a unique tuition experience!</p><cite>Grace Lau Xin Yi<br>Seaview Junior College</cite></blockquote>
    </div>

    <div class="photo photo--lecture" role="img" aria-label="Photo of students writing during a lecture in a theatre with orange seats"></div>
  </section>

  <footer class="footer">
    <span class="url" style="left:44px">www.lessonmaple.com</span>
    <span class="brand" style="left:338px">Economics At LessonMaple</span>
    <span class="url" style="left:638px">www.lessonmaple.com</span>
    <span class="brand" style="left:936px">Economics At LessonMaple</span>
  </footer>
</main>
</body>
</html>
```